Need Help having my business card stand out

I am the owner of Pine Ridge Canine Coaching and would like for my business cards to stand out. I have been trying to keep designing them myself but I can't get what I have in my head on the card. I will try my best to post templates that I like for inspirations. I want something unique but elegant. I don't want in to look cartoony or cheesy. It needs to pop in a pet shop but also in a coffee shop or gym.

Target Market(s)

Dog owners, Married ,No young kids Jr High school kids and up (maybe kids on the way) Executives, Stay at home moms/wives, Small business owners

Industry/Entity Type

Dog Training

Contact Information for Business Card

Trevor Holloway, 555-304-7162, info@pineridgecanine.example, www.pineridgecanine.example

Colors

Designer to choose colors to be used in the design.

Requirements
Must have
• my logo
Should not have
• Cursive lettering

```html
<!DOCTYPE html>
<html lang="en">
<head>
<meta charset="utf-8">
<title>Pine Ridge Canine Coaching – Business Card</title>
<link rel="stylesheet" href="https://fonts.googleapis.com/css2?family=Questrial&family=Kalam:wght@400&display=swap">
<style>
  :root {
    --backdrop: #7a7a7a;
    --card: #ffffff;
    --ink: #111111;
    --mist-dark: #b9b9b9;
    --mist-mid: #d9d9d9;
    --mist-light: #f2f2f2;
  }
  * { margin: 0; padding: 0; box-sizing: border-box; }
  html, body {
    width: 1200px; height: 1200px; overflow: hidden;
    background: var(--backdrop);
  }
  .stage { position: relative; width: 1200px; height: 1200px; }
  .card {
    position: absolute; left: 170px; width: 888px; height: 528px;
    background: var(--card); overflow: hidden; color: var(--ink);
  }
  .card--front { top: 78px; }
  .card--back { top: 638px; }

  .artwork {
    position: absolute;
  }
  .artwork--front {
    inset: 0;
    background:
      radial-gradient(ellipse 30% 55% at 24% 52%, rgba(170,170,170,.55), rgba(255,255,255,0) 70%),
      radial-gradient(ellipse 32% 58% at 74% 44%, rgba(185,185,185,.5), rgba(255,255,255,0) 70%),
      radial-gradient(ellipse 22% 30% at 50% 70%, rgba(200,200,200,.45), rgba(255,255,255,0) 70%);
  }
  .artwork--back {
    left: 20px; top: 110px; width: 470px; height: 340px;
    background:
      radial-gradient(ellipse 28% 50% at 22% 45%, rgba(140,140,140,.6), rgba(255,255,255,0) 72%),
      radial-gradient(ellipse 30% 55% at 68% 40%, rgba(150,150,150,.55), rgba(255,255,255,0) 72%),
      radial-gradient(ellipse 24% 34% at 45% 65%, rgba(170,170,170,.5), rgba(255,255,255,0) 72%);
  }

  .brand {
    position: absolute; left: 0; right: 0;
    text-align: center;
    font-family: 'Questrial', sans-serif;
    color: var(--ink);
  }
  .brand__tagline {
    top: 64px; font-size: 19px; letter-spacing: 4px; text-transform: uppercase;
  }
  .brand__name {
    top: 178px; font-size: 74px; line-height: 1.02; letter-spacing: 1px;
  }
  .brand__name span { display: block; }
  .brand__name .brand__sub { font-size: 50px; margin-top: 10px; }

  .contact {
    position: absolute; left: 470px; width: 380px; text-align: center;
  }
  .contact__brand {
    top: 92px; font-family: 'Questrial', sans-serif; font-size: 34px; line-height: 1.1;
  }
  .contact__name {
    top: 236px; font-family: 'Kalam', cursive; font-size: 46px;
  }
  .contact__phone {
    top: 326px; font-family: 'Kalam', cursive; font-size: 27px; letter-spacing: 1px;
  }
  .contact__web {
    top: 400px; font-family: 'Questrial', sans-serif; font-size: 17px; line-height: 1.4;
  }
</style>
</head>
<body>
<main class="stage">
  <section class="card card--front">
    <div class="artwork artwork--front" role="img" aria-label="Faint pencil-sketch illustration of a Doberman and a German Shepherd"></div>
    <p class="brand brand__tagline">Your Dog Trainer For Life</p>
    <h1 class="brand brand__name"><span>Pine Ridge</span><span class="brand__sub">Canine Coaching</span></h1>
  </section>

  <section class="card card--back">
    <div class="artwork artwork--back" role="img" aria-label="Pencil-sketch illustration of a Doberman, a small terrier and a German Shepherd"></div>
    <p class="contact contact__brand">Pine Ridge<br>Canine Coaching</p>
    <p class="contact contact__name">Trevor Holloway</p>
    <p class="contact contact__phone">555-304-7162</p>
    <p class="contact contact__web">info@pineridgecanine.example<br>www.pineridgecanine.example</p>
  </section>
</main>
</body>
</html>
```